Vibrant business card design for Product person in Tech

I'm a 29 y/o female Product manager and I'd like to get a business card designed I can use when networking. I'd love something that stands out. Feel free to experiment with the use of colour, maybe geometrical elements - get creative! I work in the tech industry, so looking for a design without too much of a corporate feel. <br/><br/>The business card should have room for:<br/>Name<br/>Email address<br/>LinkedIn

Target Market(s)

Tech

Contact Information for Business Card

Name
Email
LinkedIn

Colors
faa54b
00a990
33b8a4
abd037
fbee3f
e667a6
ffcf3e
f59195

```html
<!DOCTYPE html>
<html lang="en">
<head>
<meta charset="utf-8">
<title>Mirela Tovan – Business Card</title>
<link href="https://fonts.googleapis.com/css2?family=Montserrat:wght@400;500;600;700&display=swap" rel="stylesheet">
<style>
  :root {
    --page-bg: #e6e6e6;
    --card-dark: #2b2b2d;
    --card-dark-soft: #343437;
    --card-light: #ffffff;
    --accent-pink: #ea3f7b;
    --band-grey: #e4e4e4;
    --ink: #3a3a3c;
    --ink-soft: #5c5c60;
  }
  * { box-sizing: border-box; margin: 0; padding: 0; }
  html, body { width: 1200px; height: 800px; overflow: hidden; }
  body {
    background: var(--page-bg);
    font-family: "Montserrat", sans-serif;
    position: relative;
  }
  .card {
    position: absolute;
    top: 245px;
    width: 540px;
    height: 310px;
    overflow: hidden;
    box-shadow: 0 10px 28px rgba(0,0,0,0.18);
  }
  .card--front { left: 45px; background: var(--card-light); }
  .card--back { left: 615px; background: var(--card-dark); }

  .front__dark-corner {
    position: absolute; inset: 0;
    background: linear-gradient(200deg, var(--card-dark-soft), var(--card-dark));
    clip-path: polygon(40% 0, 100% 0, 100% 80%);
  }
  .name-band {
    position: absolute;
    top: 64px; left: 262px;
    width: 215px; height: 40px;
    background: var(--accent-pink);
    color: #fff;
    font-weight: 700;
    font-size: 23px;
    line-height: 40px;
    text-align: right;
    padding-right: 14px;
  }
  .role-band {
    position: absolute;
    top: 104px; left: 298px;
    width: 205px; height: 24px;
    background: var(--band-grey);
    color: var(--ink);
    font-weight: 700;
    font-size: 11px;
    letter-spacing: 0.5px;
    line-height: 24px;
    text-align: right;
    padding-right: 14px;
  }
  .brand {
    position: absolute;
    left: 38px; top: 150px;
    display: flex; align-items: center; gap: 12px;
  }
  .brand__dot {
    width: 48px; height: 48px; border-radius: 50%;
    background: var(--accent-pink);
  }
  .brand__name {
    font-weight: 700;
    font-size: 26px;
    color: var(--ink);
  }
  .contacts {
    position: absolute;
    left: 42px; top: 218px;
    list-style: none;
    display: flex; flex-direction: column; gap: 8px;
  }
  .contacts__item {
    display: flex; align-items: center; gap: 12px;
    font-weight: 500; font-size: 13px; color: var(--ink);
  }
  .contacts__icon { width: 16px; height: 16px; flex: none; }

  .back__pattern {
    position: absolute; inset: 0;
    background: radial-gradient(ellipse at center, var(--card-dark-soft), var(--card-dark) 75%);
  }
  .back__name {
    position: absolute; inset: 0;
    display: flex; align-items: center; justify-content: center;
    color: var(--accent-pink);
    font-weight: 700;
    font-size: 40px;
  }
</style>
</head>
<body>
  <section class="card card--front">
    <div class="front__dark-corner" role="img" aria-label="Dark corner panel with faint circuit-line pattern"></div>
    <div class="name-band">Mirela Tovan</div>
    <div class="role-band">PRODUCT MANAGER</div>

    <div class="brand">
      <span class="brand__dot"></span>
      <span class="brand__name">Cortex Loop</span>
    </div>

    <ul class="contacts">
      <li class="contacts__item">
        <svg class="contacts__icon" viewBox="0 0 16 16" aria-hidden="true">
          <circle cx="8" cy="5" r="3.5" fill="var(--accent-pink)"/>
          <path d="M1.5 16 C1.5 10.5 14.5 10.5 14.5 16 Z" fill="var(--accent-pink)"/>
        </svg>
        <span>Mirela Tovan</span>
      </li>
      <li class="contacts__item">
        <svg class="contacts__icon" viewBox="0 0 16 16" aria-hidden="true">
          <rect x="1" y="3.5" width="14" height="9" fill="none" stroke="var(--accent-pink)" stroke-width="1.6"/>
          <path d="M1 3.5 L8 9 L15 3.5" fill="none" stroke="var(--accent-pink)" stroke-width="1.6"/>
        </svg>
        <span>mirela_tovan@mailbox.net</span>
      </li>
      <li class="contacts__item">
        <svg class="contacts__icon" viewBox="0 0 16 16" aria-hidden="true">
          <circle cx="8" cy="8" r="7.5" fill="var(--accent-pink)"/>
        </svg>
        <span>/in/Mirela Tovan/</span>
      </li>
    </ul>
  </section>

  <section class="card card--back">
    <div class="back__pattern" role="img" aria-label="Dark background with faint circuit-line pattern"></div>
    <div class="back__name">Mirela Tovan</div>
  </section>
</body>
</html>
```